User-interface and web design for new forum-style communication platform

We developed a new forum-style communication platform specially targetting stock investors to share and discuss information on companies listed on the stock exchange.

You have complete freedom for designing the user-interface and web design. Designs should include all features listed below.

Please read the attached document for full specifications. Also attached is a mockup of the layout, but this is only directional. A mockup for the user-profile is also attached, but does not need to be designed.

This project focusses on the homepage and thread view.

The winner(s) will be asked to design the complete project. (create thread box, user profile, registering, settings...)

We are looking for a well thought out, smart design that incorporates the specifications in the attached document. Please do not hesitate to contact us if anything is not clear.

Target Market(s)

Stock investors from 25 to 60 years old (the people that are currently on investor forums)

Industry/Entity Type

Communication

Font styles to use
Sans Serif

Colors

Designer to choose colors to be used in the design.

Requirements
Must have
• Full homepage design & Thread view specified in the attached document.
Nice to have
• Create thread view
- Field for adding tags
- field for subject of the thread
- text box with basic text editing
- method for sharing media
Should not have
• Logo design.

```html
<!DOCTYPE html>
<html lang="en">
<head>
<meta charset="utf-8">
<title>Tradora – Conversations</title>
<link href="https://fonts.googleapis.com/css2?family=Roboto:wght@300;400;500&display=swap" rel="stylesheet">
<style>
:root{
  --brand:#04aeef;
  --brand-dark:#0a9fd8;
  --header-bg:#2c2c2c;
  --page-bg:#eeeeee;
  --panel-bg:#d9d9d9;
  --panel-border:#c9c9c9;
  --text:#333333;
  --muted:#999999;
  --accent:#f25a0c;
  --green:#2f8a16;
  --white:#ffffff;
  --footer:#17ace6;
}
*{box-sizing:border-box;margin:0;padding:0}
html,body{width:1200px;height:1040px;overflow:hidden}
body{position:relative;background:var(--page-bg);font-family:'Roboto',Arial,sans-serif;color:var(--text)}
.abs{position:absolute}

/* Header */
.site-header{position:absolute;left:0;top:0;width:1200px;height:93px;background:linear-gradient(#2f2f2f,#262626);border-bottom:1px solid #1b1b1b}
.brand{position:absolute;left:118px;top:24px;font-size:39px;font-weight:400;color:var(--brand);letter-spacing:.5px}
.searchbar{position:absolute;left:398px;top:28px;width:504px;height:32px;background:#3a3a3a;border:1px solid #1e1e1e;box-shadow:inset 0 1px 3px rgba(0,0,0,.5)}
.searchbar svg{position:absolute;left:7px;top:10px}
.searchbar .tags{position:absolute;left:26px;top:9px;font-size:10px;color:#8a8a8a}
.searchbar .btn{position:absolute;top:0;height:30px;width:72px;border-left:1px solid #222;font-size:10px;color:#fff;text-align:center;line-height:31px}
.searchbar .save{left:357px;color:var(--brand);box-shadow:inset 0 -3px 6px -4px var(--brand)}
.searchbar .clear{left:430px}
.notif{position:absolute;left:962px;top:34px;width:20px;height:20px;border-radius:50%;background:#ddd;border:1px solid #aaa;font-size:9px;text-align:center;line-height:19px;color:#333}
.follower-tip{position:absolute;left:940px;top:70px;width:72px;height:22px;background:#fff;border-radius:4px;font-size:10px;text-align:center;line-height:22px;color:#222}
.follower-tip:before{content:"";position:absolute;left:33px;top:-5px;border:5px solid transparent;border-top:0;border-bottom-color:#fff}
.user-menu{position:absolute;left:1001px;top:33px;width:77px;height:23px;background:#fff;border:1px solid #ccc;font-size:10px;line-height:21px;padding-left:9px}
.user-menu:after{content:"";position:absolute;left:54px;top:0;width:1px;height:21px;background:#ddd}
.user-menu .caret{position:absolute;right:8px;top:9px;border:3px solid transparent;border-top-color:#999}

/* Sidebar */
.panel{position:absolute;left:118px;width:281px;background:var(--panel-bg);border:1px solid var(--panel-border)}
.panel-title{height:32px;background:var(--brand);color:#fff;font-size:13.5px;padding-left:14px;line-height:34px}
.panel-box{position:absolute;left:13px;width:254px;background:#fff;border:1px solid #c4c4c4}
.user-search{height:40px;padding-left:34px;font-size:12px;color:var(--muted);line-height:40px}
.user-search svg{position:absolute;left:11px;top:11px}
.item-list{list-style:none;padding:10px 0 0 12px;font-size:11.5px;line-height:16.8px;color:#333}
.show-all{position:absolute;right:14px;font-size:12px;color:var(--green)}

/* Main */
.breadcrumb{position:absolute;left:422px;top:128px;font-size:12px;color:#222}
.breadcrumb span{margin-right:14px}
.breadcrumb .home{color:var(--brand)}
.breadcrumb .sep{color:#333;margin-right:14px}
.tabs{position:absolute;left:422px;top:159px;width:657px;height:44px;background:var(--brand)}
.tab{position:absolute;top:0;height:44px;color:#fff;font-size:12px;text-align:center;line-height:44px;border-right:1px solid #1a9bd0}
.tab.active{color:#222}
.create-btn{position:absolute;left:567px;top:10px;width:81px;height:24px;background:#fff;border:1px solid #bbb;font-size:11.5px;text-align:center;line-height:22px;color:#222}
.sort-pop{position:absolute;left:429px;top:203px;width:73px;height:38px;background:#fff;border:1px solid #bbb;border-radius:6px;font-size:9.5px;text-align:center;line-height:14px;padding-top:5px;color:#222}
.sort-pop:before{content:"";position:absolute;left:32px;top:-5px;border:5px solid transparent;border-top:0;border-bottom-color:#fff}

.thread{position:absolute;left:421px;width:658px;height:215px;background:#fff;border:1px solid #cfcfcf}
.thumb{position:absolute;background:linear-gradient(135deg,#0d2a4a 0%,#1d4f8a 35%,#2e8a4c 60%,#0b1d3a 100%)}
.thread .thumb{left:12px;top:14px;width:100px;height:85px}
.thread h2{position:absolute;left:130px;top:19px;font-size:11.5px;font-weight:400;color:var(--accent)}
.thread .byline{position:absolute;left:130px;top:38px;font-size:9.5px;color:var(--green)}
.thread p{position:absolute;left:130px;top:60px;width:515px;font-size:9px;line-height:19.2px;color:#333}
.thread .stats{position:absolute;left:12px;top:178px;font-size:9.5px;color:var(--brand);display:flex;align-items:center}
.stats .more{color:var(--accent);margin-right:9px}
.stats svg{margin-right:6px}
.stats .gap{margin-right:12px}
.action{position:absolute;top:170px;width:63px;height:25px;background:var(--brand);color:#fff;font-size:10px;text-align:center;line-height:25px}
.meta{position:absolute;left:421px;font-size:9.5px;color:var(--brand)}
.meta .dot,.meta .time{color:#aaa}
.comment-row .thumb{left:433px;width:56px;height:48px}
.comment-input{position:absolute;left:506px;width:573px;height:38px;background:#fff;border:1px solid var(--brand);font-size:9.5px;color:#999;line-height:36px;padding-left:14px}
.comment-input svg{position:absolute;right:12px;top:10px}

/* Footer */
.site-footer{position:absolute;left:0;top:955px;width:1200px;height:85px;background:var(--footer);color:#fff}
.copyright{position:absolute;left:118px;top:35px;font-size:11.5px}
.social{position:absolute;top:25px;width:30px;height:30px;border-radius:50%;background:#e8e8e8;border:2px solid #fff;box-shadow:0 1px 2px rgba(0,0,0,.3)}
</style>
</head>
<body>

<header class="site-header">
  <div class="brand">Tradora</div>
  <div class="searchbar">
    <svg width="11" height="11" viewBox="0 0 11 11"><circle cx="4.5" cy="4.5" r="3.5" fill="none" stroke="#ddd" stroke-width="1.5"/><line x1="7" y1="7" x2="10" y2="10" stroke="#ddd" stroke-width="1.5"/></svg>
    <span class="tags"># lumacorp &nbsp; #vireon</span>
    <div class="btn save">Save</div>
    <div class="btn clear">Clear</div>
  </div>
  <div class="notif">3</div>
  <div class="follower-tip">1 new follower</div>
  <div class="user-menu">User<span class="caret"></span></div>
</header>

<aside>
  <section class="panel" style="top:121px;height:105px">
    <div class="panel-title">Users</div>
    <div class="panel-box user-search" style="top:44px">
      <svg width="17" height="17" viewBox="0 0 17 17"><circle cx="7" cy="7" r="5.5" fill="none" stroke="#111" stroke-width="2"/><line x1="11" y1="11" x2="15.5" y2="15.5" stroke="#111" stroke-width="2.2"/></svg>
      Search
    </div>
  </section>

  <section class="panel" style="top:251px;height:208px">
    <div class="panel-title">Saved Filters</div>
    <div class="panel-box" style="top:45px;height:121px">
      <ul class="item-list"><li>Item Name</li><li>Item Name</li><li>Item Name</li><li>Item Name</li><li>Item Name</li><li>Item Name</li></ul>
    </div>
    <span class="show-all" style="top:179px">Show all</span>
  </section>

  <section class="panel" style="top:484px;height:208px">
    <div class="panel-title" style="height:36px;line-height:36px">Papular Tags</div>
    <div class="panel-box" style="top:46px;height:121px">
      <ul class="item-list"><li>Item Name</li><li>Item Name</li><li>Item Name</li><li>Item Name</li><li>Item Name</li><li>Item Name</li></ul>
    </div>
    <span class="show-all" style="top:180px">Show all</span>
  </section>

  <section class="panel" style="top:718px;height:208px">
    <div class="panel-title" style="height:34px;line-height:35px">Papular Contributors</div>
    <div class="panel-box" style="top:45px;height:121px">
      <ul class="item-list"><li>Item Name</li><li>Item Name</li><li>Item Name</li><li>Item Name</li><li>Item Name</li><li>Item Name</li></ul>
    </div>
    <span class="show-all" style="top:178px">Show all</span>
  </section>
</aside>

<main>
  <nav class="breadcrumb"><span class="home">Home</span><span class="sep">›</span><span>Conversations</span><span class="sep">›</span><span>Public</span><span class="sep">›</span><span>lumacorp #vireon</span></nav>

  <div class="tabs">
    <div class="tab active" style="left:0;width:81px">Public</div>
    <div class="tab" style="left:81px;width:89px">Following</div>
    <div class="tab" style="left:170px;width:81px">Conatcts</div>
    <div class="create-btn">Create thread</div>
  </div>
  <div class="sort-pop">Recent<br>Popular</div>

  <!-- Thread 1 -->
  <article class="thread" style="top:234px">
    <div class="thumb" role="img" aria-label="Stock exchange ticker board photo"></div>
    <h2>Lorem ipsum dolor sit amet, consectetur adipiscing elit.</h2>
    <div class="byline">Posted by Adrian on 01/01/2014</div>
    <p>Lorem ipsum dolor sit amet, consectetur adipiscing elit. Nulla convallis egestas rhoncus. Donec facilisis fermentum sem, ac viverra ante luctus vel. Donec vel mauris quam. Aliquam pellentesque pellentesque turpis, ut bibendum sapien sollicitudin nec. Pellentesque posuere ornare placerat. Suspendisse potenti. Quisque massa tortor, tristique non tristique at, luctus sed massa. Donec libero eros, mollis ac...Lorem ipsum dolor sit amet, consectetur adipiscing elit. Nulla convallis egestas rhoncus. Donec facilisis fermentum sem, ac viverra ante luctus vel.</p>
    <div class="stats">
      <span class="more">Read More+</span>
      <svg width="12" height="9" viewBox="0 0 12 9"><path d="M5 0 L0 4 L5 8 V5.5 C8 5.5 10 6.5 12 9 C11 5 8.5 3 5 2.8Z" fill="#222"/></svg>
      <span class="gap">12 Reply</span>
      <svg width="15" height="9" viewBox="0 0 15 9"><ellipse cx="7.5" cy="4.5" rx="7.5" ry="4.5" fill="#111"/><circle cx="7.5" cy="4.5" r="2.4" fill="#fff"/><circle cx="7.5" cy="4.5" r="1.3" fill="#111"/></svg>
      <span style="margin-left:6px">250 Views</span>
    </div>
    <div class="action" style="left:429px">Reply</div>
    <div class="action" style="left:502px">Share</div>
    <div class="action" style="left:575px">Favourite</div>
  </article>
  <div class="meta" style="top:475px">Like <span class="dot">•</span> Comment <span class="dot">•</span> Share <span class="dot">•</span> <span class="time">4hours ago</span></div>
  <div class="comment-row">
    <div class="thumb" style="top:502px" role="img" aria-label="Commenter avatar, stock ticker photo"></div>
    <div class="comment-input" style="top:502px">Write a comment.....
      <svg width="24" height="17" viewBox="0 0 24 17"><rect x="0" y="3" width="24" height="14" rx="2" fill="#aaa"/><rect x="8" y="0" width="8" height="4" rx="1" fill="#aaa"/><circle cx="12" cy="10" r="4.5" fill="#fff"/><circle cx="12" cy="10" r="3" fill="#aaa"/></svg>
    </div>
  </div>

  <!-- Thread 2 -->
  <article class="thread" style="top:580px">
    <div class="thumb" role="img" aria-label="Stock exchange ticker board photo"></div>
    <h2>Lorem ipsum dolor sit amet, consectetur adipiscing elit.</h2>
    <div class="byline">Posted by Adrian on 01/01/2014</div>
    <p>Lorem ipsum dolor sit amet, consectetur adipiscing elit. Nulla convallis egestas rhoncus. Donec facilisis fermentum sem, ac viverra ante luctus vel. Donec vel mauris quam. Aliquam pellentesque pellentesque turpis, ut bibendum sapien sollicitudin nec. Pellentesque posuere ornare placerat. Suspendisse potenti. Quisque massa tortor, tristique non tristique at, luctus sed massa. Donec libero eros, mollis ac...Lorem ipsum dolor sit amet, consectetur adipiscing elit. Nulla convallis egestas rhoncus. Donec facilisis fermentum sem, ac viverra ante luctus vel.</p>
    <div class="stats">
      <span class="more">Read More+</span>
      <svg width="12" height="9" viewBox="0 0 12 9"><path d="M5 0 L0 4 L5 8 V5.5 C8 5.5 10 6.5 12 9 C11 5 8.5 3 5 2.8Z" fill="#222"/></svg>
      <span class="gap">12 Reply</span>
      <svg width="15" height="9" viewBox="0 0 15 9"><ellipse cx="7.5" cy="4.5" rx="7.5" ry="4.5" fill="#111"/><circle cx="7.5" cy="4.5" r="2.4" fill="#fff"/><circle cx="7.5" cy="4.5" r="1.3" fill="#111"/></svg>
      <span style="margin-left:6px">250 Views</span>
    </div>
    <div class="action" style="left:429px">Reply</div>
    <div class="action" style="left:502px">Share</div>
    <div class="action" style="left:575px">Favourite</div>
  </article>
  <div class="meta" style="top:821px">Like <span class="dot">•</span> Comment <span class="dot">•</span> Share <span class="dot">•</span> <span class="time">4hours ago</span></div>
  <div class="comment-row">
    <div class="thumb" style="top:848px" role="img" aria-label="Commenter avatar, stock ticker photo"></div>
    <div class="comment-input" style="top:848px">Write a comment.....
      <svg width="24" height="17" viewBox="0 0 24 17"><rect x="0" y="3" width="24" height="14" rx="2" fill="#aaa"/><rect x="8" y="0" width="8" height="4" rx="1" fill="#aaa"/><circle cx="12" cy="10" r="4.5" fill="#fff"/><circle cx="12" cy="10" r="3" fill="#aaa"/></svg>
    </div>
  </div>
</main>

<footer class="site-footer">
  <div class="copyright">© 2014 Kestrel Labs All Rights Reserved</div>
  <div class="social" style="left:976px"></div>
  <div class="social" style="left:1012px"></div>
  <div class="social" style="left:1047px"></div>
</footer>

</body>
</html>
```